Home page concept, possible logo colour change

There is no need to code a home page, we are just looking for concept ideas.
We have had a logo designed for a new company we are starting named Corvenhall Aluminium Windows & Doors. We are manufacturing bullet resistant window frames. We have had logo designed, we like the concept of the design, but the current colours (black and red) may not be the best option, especially when designing the website home page, and how it interacts with the logo colours. I have also attached the first draft of the home page which we are not happy with. The overall design/navigation is good, we have issues with the darkened out primary image and also the amount of red on the page, it just doesn't feel right. As mentioned before we are happy to look at colour changes to the logo.
Number of Pages Required
1 page
Look and feel
Each slider illustrates characteristics of the customer's brand and the style your logo design should communicate.

```html
<!DOCTYPE html>
<html lang="en">
<head>
<meta charset="utf-8">
<title>Corvenhall Aluminium Windows &amp; Doors</title>
<link rel="stylesheet" href="https://fonts.googleapis.com/css2?family=DM+Sans:wght@400;500;700&display=swap">
<style>
  :root {
    --bg: #f6f6f6;
    --orange: #fb5d1e;
    --orange-light: #f86c31;
    --red: #d9301a;
    --ink: #2c2c2c;
    --ink-soft: #3a3a3a;
    --white: #ffffff;
    --rule: #ececec;
    --icon-disc: #e8e8e8;
  }
  * { box-sizing: border-box; margin: 0; padding: 0; }
  html, body { width: 1200px; height: 745px; overflow: hidden; }
  body { background: var(--bg); font-family: "DM Sans", sans-serif; color: var(--ink); position: relative; }

  .hero-shape { position: absolute; inset: 0; width: 1200px; height: 745px; }

  .brand { position: absolute; left: 233px; top: 18px; display: flex; align-items: center; gap: 8px; }
  .brand-dot { width: 12px; height: 12px; border-radius: 50%; background: var(--red); }
  .brand-name { font-weight: 700; font-size: 25px; color: #1a1a1a; line-height: 1; letter-spacing: -0.5px; }
  .brand-tag { display: block; font-weight: 700; font-size: 6.5px; letter-spacing: 0.6px; color: #1a1a1a; margin-top: 3px; }

  .main-nav { position: absolute; top: 22px; left: 566px; display: flex; align-items: center; gap: 20px; }
  .main-nav a { color: var(--white); text-decoration: none; font-size: 13.5px; font-weight: 500; }
  .main-nav .nav-cta { background: var(--white); color: var(--orange); padding: 8px 14px; margin-left: 2px; box-shadow: 0 4px 12px rgba(0,0,0,0.18); }

  .product-photo { position: absolute; left: 662px; top: 65px; width: 238px; height: 505px;
    background: linear-gradient(180deg, #f3f3f3 0%, #e4e4e4 70%, rgba(240,240,240,0) 100%); }
  .product-photo .glass { position: absolute; left: 34px; top: 38px; width: 170px; height: 395px;
    background: linear-gradient(160deg, #e97a53 0%, #e86a44 60%, #f1efee 100%); opacity: .9; }

  .hero-copy { position: absolute; left: 232px; top: 220px; width: 320px; }
  .hero-title { color: var(--orange); font-weight: 500; font-size: 31.5px; line-height: 1.1; }
  .hero-text { margin-top: 14px; font-size: 13px; line-height: 1.45; color: var(--ink-soft); }
  .hero-btn { display: inline-flex; align-items: center; justify-content: center; gap: 8px; margin-top: 20px;
    width: 199px; height: 40px; border-radius: 20px; background: var(--orange); color: var(--white);
    font-size: 13px; font-weight: 500; text-decoration: none; box-shadow: 0 6px 14px rgba(0,0,0,0.15); }

  .features-rule { position: absolute; left: 0; right: 0; top: 592px; border-top: 1px solid var(--rule); }
  .features { position: absolute; top: 566px; left: 0; right: 0; }
  .feature { position: absolute; width: 200px; text-align: center; }
  .feature-icon { position: relative; width: 56px; height: 56px; margin: 0 auto; }
  .feature-icon::before { content: ""; position: absolute; left: 4px; top: 16px; width: 28px; height: 28px; border-radius: 50%; background: var(--icon-disc); }
  .feature-icon svg { position: relative; }
  .feature-title { color: var(--orange); font-weight: 500; font-size: 16px; margin-top: 8px; }
  .feature-text { font-size: 10px; line-height: 1.85; margin-top: 5px; color: var(--ink); }
</style>
</head>
<body>
  <svg class="hero-shape" viewBox="0 0 1200 745" aria-hidden="true">
    <defs>
      <linearGradient id="heroGrad" x1="0" y1="0" x2="1" y2="0.4">
        <stop offset="0" stop-color="#f86c31"/>
        <stop offset="1" stop-color="#d9301a"/>
      </linearGradient>
    </defs>
    <path d="M562 0 C 610 210, 760 520, 1030 528 L1200 528 L1200 0 Z" fill="url(#heroGrad)"/>
  </svg>

  <header>
    <div class="brand">
      <span class="brand-dot"></span>
      <div>
        <span class="brand-name">Corvenhall</span>
        <span class="brand-tag">ALUMINIUM WINDOWS &amp; DOORS</span>
      </div>
    </div>
    <nav class="main-nav">
      <a href="#">Home</a>
      <a href="#">Our Products</a>
      <a href="#">Why Corvenhall</a>
      <a href="#" class="nav-cta">Make an Enquiry</a>
    </nav>
  </header>

  <div class="product-photo" role="img" aria-label="Photograph of a white aluminium double door with bullet resistant glass panels">
    <div class="glass"></div>
  </div>

  <section class="hero-copy">
    <h1 class="hero-title">Bullet Resistant<br>Windows &amp; Doors</h1>
    <p class="hero-text">Lorem ipsum dolor sit amet, consectetur adipiscing elit, sed do eiusmod tempor incididunt ut labore et dolore magna aliqua.</p>
    <a href="#" class="hero-btn">Learn More
      <svg width="12" height="12" viewBox="0 0 12 12" fill="none" stroke="#fff" stroke-width="1.6"><path d="M1 6h10M6.5 1.5 11 6l-4.5 4.5"/></svg>
    </a>
  </section>

  <div class="features-rule"></div>
  <section class="features">
    <div class="feature" style="left:276px">
      <div class="feature-icon">
        <svg width="56" height="56" viewBox="0 0 56 56" fill="none" stroke="#e2522a" stroke-width="2.2" stroke-linejoin="round">
          <path d="M28 6 L45 12 C45 30 38 42 28 48 C18 42 11 30 11 12 Z"/>
          <path d="M28 6V48M11.5 22H44.5"/>
        </svg>
      </div>
      <h3 class="feature-title">Premium Protection</h3>
      <p class="feature-text">Lorem ipsum dolor sit amet,<br>consectetur adipiscing elit,<br>sed do eiusmod.</p>
    </div>
    <div class="feature" style="left:501px">
      <div class="feature-icon">
        <svg width="56" height="56" viewBox="0 0 56 56" fill="none" stroke="#e2522a" stroke-width="2">
          <path d="M4 2 L54 8 V50 L4 54 Z"/>
          <path d="M16 3.5V53M29 5V52M42 6.5V51M4 20L54 23M4 36L54 37M32 44L54 45"/>
        </svg>
      </div>
      <h3 class="feature-title">Aesthetic Design</h3>
      <p class="feature-text">Lorem ipsum dolor sit amet,<br>consectetur adipiscing elit,<br>sed do eiusmod.</p>
    </div>
    <div class="feature" style="left:728px">
      <div class="feature-icon">
        <svg width="64" height="56" viewBox="0 0 64 56" fill="none" stroke="#e2522a" stroke-width="2.2" stroke-linejoin="round">
          <rect x="12" y="10" width="36" height="38" rx="2"/>
          <path d="M24 10V24H34V10M50 24H60M50 36H60"/>
        </svg>
      </div>
      <h3 class="feature-title">Prompt Delivery</h3>
      <p class="feature-text">Lorem ipsum dolor sit amet,<br>consectetur adipiscing elit,<br>sed do eiusmod.</p>
    </div>
  </section>
</body>
</html>
```